Design The Loomfield Hompage

See powerpoint

Industry/Entity Type

SAAS data product

Coding

Coded - Design and coding required

Number of Pages Required

4 page

Font styles to use
Sans Serif

```html
<!DOCTYPE html>
<html lang="en">
<head>
<meta charset="utf-8">
<title>The Loomfield – Public Data Made Easy</title>
<link href="https://fonts.googleapis.com/css2?family=Poppins:wght@400;500;600;700&display=swap" rel="stylesheet">
<style>
:root{
  --blue:#0a6bc1;
  --orange:#f7931e;
  --ink:#111111;
  --text:#555555;
  --soft:#fff1e2;
  --footer:#1c1c1c;
  --footer-field:#2c2c2c;
  --line:#d9d9d9;
  --white:#ffffff;
}
*{margin:0;padding:0;box-sizing:border-box}
html,body{width:1200px;height:2561px;overflow:hidden}
body{position:relative;font-family:'Poppins',sans-serif;color:var(--ink);background:var(--white)}
.abs{position:absolute}

.top-rule{left:0;top:0;width:1200px;height:3px;background:var(--blue)}
.brand{left:110px;top:24px;display:flex;align-items:center;gap:12px}
.brand-dot{width:44px;height:44px;border-radius:50%;background:var(--orange)}
.brand-name{font-weight:600;font-size:23px;color:var(--ink);letter-spacing:.3px}
.nav{top:38px;left:0;width:1200px;height:20px}
.nav a{position:absolute;font-size:15px;color:#333;text-decoration:none}
.nav a.active{color:var(--blue)}
.header-rule{left:110px;top:100px;width:985px;height:1px;background:var(--line)}

.hero-eyebrow{left:108px;top:128px;font-size:28px;font-weight:600;color:var(--orange)}
.hero-title{left:105px;top:178px;font-size:61px;font-weight:700;line-height:68px;letter-spacing:.5px}
.hero-copy{left:688px;top:141px;width:415px;font-size:14px;line-height:28px;color:var(--text)}
.btn{display:flex;align-items:center;justify-content:center;background:var(--blue);color:var(--white);font-weight:600;font-size:15px;border-radius:22px}
.hero-btn{left:689px;top:245px;width:231px;height:43px}
.hero-visual{left:0;top:362px;width:1200px;height:568px;background:linear-gradient(100deg,#1b2c44 0%,#284a6b 45%,#1d3a5c 70%,#2a4d72 100%)}

.intro{left:180px;top:991px;width:840px;text-align:center;font-size:15px;font-weight:600;line-height:30px;color:#222}
.card{top:1087px;width:235px;height:301px;background:var(--white);border-radius:20px;box-shadow:0 6px 22px rgba(0,0,0,.07);text-align:center}
.card-icon{width:68px;height:68px;border-radius:50%;background:var(--soft);margin:39px auto 16px;display:flex;align-items:center;justify-content:center}
.card p{font-size:12.5px;line-height:24px;color:var(--text);padding:0 18px}
.pager{width:32px;height:32px;border-radius:50%;background:var(--soft);display:flex;align-items:center;justify-content:center;top:1424px}

.about-visual{left:110px;top:1502px;width:470px;height:470px;border-radius:50%;background:radial-gradient(circle at 55% 45%,#1f5fb0 0%,#123a7a 55%,#070f22 100%)}
.about-inset{left:360px;top:1753px;width:246px;height:246px;border-radius:50%;border:6px solid var(--white);background:radial-gradient(circle at 50% 45%,#d9dde4 0%,#6c7f9c 35%,#1a2b48 75%);box-shadow:0 4px 14px rgba(0,0,0,.15)}
.about-eyebrow{left:679px;top:1548px;font-size:25px;font-weight:600;color:var(--orange)}
.about-title{left:679px;top:1585px;font-size:42px;font-weight:700}
.about-copy{left:679px;top:1651px;width:420px;font-size:14.5px;line-height:30px;color:var(--text)}
.about-copy p+p{margin-top:13px}
.about-btn{left:679px;top:1896px;width:138px;height:43px}

.footer{left:0;top:2100px;width:1200px;height:461px;background:var(--footer);color:var(--white)}
.footer-brand{left:110px;top:62px;display:flex;align-items:center;gap:20px}
.footer-brand .brand-dot{width:70px;height:70px}
.footer-brand .brand-name{color:var(--white);font-size:40px}
.news-label{left:648px;top:64px;font-size:12px;font-weight:600}
.news-field{left:648px;top:94px;width:448px;height:52px;border-radius:26px;background:var(--footer-field);display:flex;align-items:center;padding-left:31px;font-size:13.5px;font-weight:500}
.news-send{right:7px;top:7px;width:38px;height:38px;border-radius:50%;background:var(--orange);display:flex;align-items:center;justify-content:center}
.footer-rule{left:110px;top:180px;width:986px;height:1px;background:#3a3a3a}
.col{top:214px}
.col h3{font-size:20px;font-weight:600;margin-bottom:14px}
.col li{list-style:none;font-size:14.5px;line-height:32px;display:flex;align-items:flex-start;gap:14px}
.bullet{flex:none;width:12px;height:12px;border-radius:50%;border:2px solid var(--white);position:relative;top:10px}
.bullet::after{content:"";position:absolute;left:2px;top:2px;width:4px;height:4px;border-radius:50%;background:var(--white)}
.social{display:flex;gap:8px;margin:6px 0 0 26px}
.social span{width:31px;height:31px;border-radius:50%;background:var(--orange)}
.copyright{left:0;top:437px;width:1200px;text-align:center;font-size:11px}
</style>
</head>
<body>
<div class="abs top-rule"></div>

<header>
  <div class="abs brand"><span class="brand-dot"></span><span class="brand-name">THE LOOMFIELD</span></div>
  <nav class="abs nav">
    <a class="active" style="left:480px">Home</a>
    <a style="left:579px">About Us</a>
    <a style="left:698px">Data</a>
    <a style="left:788px">Documentation</a>
    <a style="left:956px">Pricing</a>
    <a style="left:1060px">Blog</a>
  </nav>
  <div class="abs header-rule"></div>
</header>

<section>
  <div class="abs hero-eyebrow">THE LOOMFIELD</div>
  <h1 class="abs hero-title">PUBLIC<br>DATA MADE EASY</h1>
  <p class="abs hero-copy">From demographics to economics, from weather to health, on country level or community level. The Loomfield collects many public data sources and organizes it for you.</p>
  <a class="abs btn hero-btn">Register &amp; Start For Free</a>
  <div class="abs hero-visual" role="img" aria-label="Person working on a laptop beside a network diagram of SaaS cloud services"></div>
</section>

<section>
  <p class="abs intro">As a data scientist or engineer you always are looking for getting more data in with more efficiency. This is exactly what The Loomfield is making possible for you</p>

  <div class="abs card" style="left:102px">
    <div class="card-icon"><svg width="38" height="38" viewBox="0 0 38 38" fill="none" stroke="#f7931e" stroke-width="1.6"><rect x="3" y="4" width="9" height="12"/><rect x="14.5" y="4" width="9" height="12"/><rect x="26" y="4" width="9" height="12"/><path d="M19 18v8M7 16v4h24v-4"/><path d="M8 28l11-4 11 4-11 5z"/></svg></div>
    <p>Public data comes from many sources, all with their own data format and interface. No longer worry about these differences, The Loomfield collects and standardizes it for you.</p>
  </div>
  <div class="abs card" style="left:358px">
    <div class="card-icon"><svg width="38" height="38" viewBox="0 0 38 38" fill="none" stroke="#f7931e" stroke-width="1.6"><path d="M10 20a6 6 0 0 1 1-12 8 8 0 0 1 15 2 5 5 0 0 1 1 10z"/><rect x="13" y="13" width="12" height="9"/><path d="M16 22v9M22 22v9M19 22v12M12 31h14"/></svg></div>
    <p>Use the loomfield API to combine Public data with your own comapny data and create value for your business.</p>
  </div>
  <div class="abs card" style="left:614px">
    <div class="card-icon"><svg width="38" height="38" viewBox="0 0 38 38" fill="none" stroke="#f7931e" stroke-width="1.6"><ellipse cx="15" cy="8" rx="10" ry="4"/><path d="M5 8v18c0 2 4 4 10 4M25 8v8M5 14c0 2 4 4 10 4s10-2 10-4M5 20c0 2 4 4 10 4"/><circle cx="27" cy="26" r="4"/><circle cx="27" cy="26" r="8" stroke-dasharray="3 2"/></svg></div>
    <p>For all data we give you the legends as well as the sources from which we retrieve the data. So you always know what the data is exactly about.</p>
  </div>
  <div class="abs card" style="left:870px">
    <div class="card-icon"><svg width="38" height="38" viewBox="0 0 38 38" fill="none" stroke="#f7931e" stroke-width="1.6"><rect x="4" y="4" width="22" height="8" rx="2"/><rect x="4" y="14" width="22" height="8" rx="2"/><rect x="4" y="24" width="14" height="8" rx="2"/><path d="M28 20l6 2v5c0 4-3 6-6 7-3-1-6-3-6-7v-5z"/><path d="M25 27l2 2 4-4"/></svg></div>
    <p>Use the latest public data in your data pipeline as the loomfield makes daily updates to the data. You no longer need to worry about multiple differnt data sources.</p>
  </div>

  <div class="abs pager" style="left:566px"><svg width="10" height="10" viewBox="0 0 10 10" fill="none" stroke="#f7931e" stroke-width="1.5"><path d="M5 2L2 5l3 3M8 2L5 5l3 3"/></svg></div>
  <div class="abs pager" style="left:604px"><svg width="10" height="10" viewBox="0 0 10 10" fill="none" stroke="#f7931e" stroke-width="1.5"><path d="M2 2l3 3-3 3M5 2l3 3-3 3"/></svg></div>
</section>

<section>
  <div class="abs about-visual" role="img" aria-label="Blue cloud shape over glowing server data columns"></div>
  <div class="abs about-inset" role="img" aria-label="White cloud above a server rack with blue cables"></div>
  <div class="abs about-eyebrow">ABOUT US</div>
  <h2 class="abs about-title">WHO WE ARE</h2>
  <div class="abs about-copy">
    <p>Sed ut perspiciatis unde omnis iste natus error sit voluptatem accusantium doloremque laudantium, totam rem aperiam, eaque ipsa quae ab illo inventore veritatis et quasi architecto beatae vitae dicta sunt explicabo. Nemo enim ipsam voluptatem quia voluptas</p>
    <p>Nemo enim ipsam voluptatem quia voluptas sit aspern atur aut odit aut fugit, sed quia consequun</p>
  </div>
  <a class="abs btn about-btn">Read More</a>
</section>

<footer class="abs footer">
  <div class="abs footer-brand"><span class="brand-dot"></span><span class="brand-name">THE LOOMFIELD</span></div>
  <div class="abs news-label">JOIN OUR NEWSLETTER</div>
  <div class="abs news-field">Enter Email Address
    <span class="abs news-send"><svg width="16" height="16" viewBox="0 0 16 16" fill="#fff"><path d="M15 1L1 7l5 2 2 6z"/></svg></span>
  </div>
  <div class="abs footer-rule"></div>

  <div class="abs col" style="left:110px"><h3>QUICK LINKS</h3><ul>
    <li><span class="bullet"></span>Pricing</li><li><span class="bullet"></span>Documentation</li><li><span class="bullet"></span>Data</li><li><span class="bullet"></span>Blog</li></ul></div>
  <div class="abs col" style="left:359px"><h3>OUR PRODUCT</h3><ul>
    <li><span class="bullet"></span>Introduction</li><li><span class="bullet"></span>The datamodels</li><li><span class="bullet"></span>The API</li><li><span class="bullet"></span>The SDK</li></ul></div>
  <div class="abs col" style="left:604px"><h3>THE COMPANY</h3><ul>
    <li><span class="bullet"></span>About</li><li><span class="bullet"></span>Frequently Asked Questions</li><li><span class="bullet"></span>Privacy Policy</li><li><span class="bullet"></span>Cookie Policy</li><li><span class="bullet"></span>Terms of Service</li></ul></div>
  <div class="abs col" style="left:900px"><h3>CONTACT US</h3><ul>
    <li><span class="bullet"></span>Email:<br>info@the-loomfield.io</li><li><span class="bullet"></span>Follow us on:</li></ul>
    <div class="social"><span aria-label="Social profile"></span><span aria-label="Social profile"></span></div></div>

  <div class="abs copyright">(C) Copyright 2024 | All Rights Reserved</div>
</footer>
</body>
</html>
```